Business Card for Industrial Distributor

We need a business card design for an industrial distributor. We sell machine parts for the manufacturing and oil industry. We would like the cards to look clean and modern but with a touch of industry.

Our colors are blue/white.

Please feel free to visit our website www.krovelmint.com

Target Market(s)

mexican manufacturers in the automobile/aerospace industry

Industry/Entity Type

Industrial

Colors
ffffff
0555a3

```html
<!DOCTYPE html>
<html lang="en">
<head>
<meta charset="utf-8">
<title>Krovelmint Business Card</title>
<link href="https://fonts.googleapis.com/css2?family=PT+Sans:wght@400;700&display=swap" rel="stylesheet">
<style>
  :root {
    --stage: #000000;
    --card-front: #212a4a;
    --card-back: #c0c1c3;
    --ink-light: #ffffff;
    --ink-soft: #e4e7f0;
    --divider: rgba(255,255,255,0.35);
    --brand-blue: #2a3c9e;
    --brand-blue-mark: #1f5bbf;
  }
  * { margin: 0; padding: 0; box-sizing: border-box; }
  html, body {
    width: 1200px; height: 900px; overflow: hidden;
    background: var(--stage);
    font-family: "PT Sans", Arial, sans-serif;
  }
  .canvas { position: relative; width: 1200px; height: 900px; }
  .card {
    position: absolute; top: 271px;
    width: 457px; height: 281px; border-radius: 12px;
  }
  .card--front { left: 137px; background: var(--card-front); }
  .card--back { left: 626px; background: var(--card-back); }

  .brand { position: absolute; display: flex; align-items: center; }
  .brand__dot { border-radius: 50%; flex: none; }
  .brand__name { font-weight: 700; line-height: 1; }

  .card--front .brand { left: 23px; top: 112px; }
  .card--front .brand__dot { width: 44px; height: 44px; background: var(--ink-light); margin-right: 8px; }
  .card--front .brand__name { color: var(--ink-light); font-size: 30px; }

  .card--back .brand { left: 53px; top: 103px; }
  .card--back .brand__dot { width: 74px; height: 74px; background: var(--brand-blue-mark); margin-right: 12px; }
  .card--back .brand__name { color: var(--brand-blue); font-size: 50px; }

  .divider { position: absolute; left: 252px; top: 50px; width: 1px; height: 185px; background: var(--divider); }

  .contact { position: absolute; left: 266px; top: 48px; color: var(--ink-light); }
  .contact__name { font-size: 17px; font-weight: 700; line-height: 20px; }
  .contact__role { font-size: 14px; line-height: 18px; color: var(--ink-soft); }
  .contact__list { list-style: none; margin-top: 24px; }
  .contact__item { display: flex; align-items: center; font-size: 14.5px; line-height: 17.5px; }
  .contact__item svg { width: 9px; height: 9px; margin-right: 9px; flex: none; fill: var(--ink-light); }
  .contact__address { margin-top: 22px; font-size: 13px; line-height: 17px; font-style: normal; }
</style>
</head>
<body>
<main class="canvas">
  <section class="card card--front">
    <div class="brand">
      <span class="brand__dot"></span>
      <span class="brand__name">Krovelmint</span>
    </div>
    <div class="divider"></div>
    <div class="contact">
      <p class="contact__name">Marcus Hale</p>
      <p class="contact__role">Administrator</p>
      <ul class="contact__list">
        <li class="contact__item">
          <svg viewBox="0 0 10 10"><path d="M1 4 Q5 0 9 4 L7.5 5 L6.5 3.8 H3.5 L2.5 5 Z M2.5 5.5 H7.5 L8.5 9 H1.5 Z"/></svg>415-738-0026
        </li>
        <li class="contact__item">
          <svg viewBox="0 0 10 10"><path d="M3 0.5 H7 V9.5 H3 Z M3.8 1.5 V7.5 H6.2 V1.5 Z"/></svg>415-738-06182
        </li>
        <li class="contact__item">
          <svg viewBox="0 0 10 10"><path d="M0.5 2 H9.5 V8 H0.5 Z M1.5 3 L5 5.5 L8.5 3 Z"/></svg>info@krovelmint.com
        </li>
        <li class="contact__item">
          <svg viewBox="0 0 10 10"><circle cx="5" cy="5" r="4.5"/></svg>www.krovelmint.com
        </li>
      </ul>
      <address class="contact__address">248 W. Harlow Suite 910.<br>Denver, Colorado 80204</address>
    </div>
  </section>
  <section class="card card--back">
    <div class="brand">
      <span class="brand__dot"></span>
      <span class="brand__name">Krovelmint</span>
    </div>
  </section>
</main>
</body>
</html>
```